Fennick Executive Search - New Business Card Design Project

We are an executive search firm called Fennick Executive Search based in the UK. We require a custom design for a business card. We're looking to convey a professional service to executives for executive search recruitment services. In terms of colours, we like dark blues and grays (maybe even silver incorporated somewhere if we go for a foiled type of card) but we're open to your artistic flare. See our current logo in attachments. We are totally open on design so long as the design is slick and professional.
Updates

Thanks for all your contributions of various designs. I have to say the quality of work has been amazing which is going to make our job quite difficult in the coming days on making a decision. Thanks to you all that have taken the time to submit designs thus far. We'll keep on reviewing and try to narrow down our selection as soon as possible.

Target Market(s)

Executive Search

Industry/Entity Type

Recruitment

Contact Information for Business Card

Fennick Executive Search,
Exclusively Sourcing & Hiring Senior Leaders
Gordon Pellbury, Managing Director,
07823 906417
0117 486 7132
gordon@fennickexecutive.co.uk
fennickexecutive.co.uk
58 Lindmoor Court, Hatherley Road, Bristol, BS32 9QJ

Font styles to use
Sans Serif
Other font styles liked:
• Roboto (which is used in our logo)

Requirements
Must have
• Our logo (It has a subtle fade on it from #02071d at top to #333649 at bottom)
• The logo can be on one side or both sides
• Must be elegant and professional
• We have 2nd slogan CONSULT | INSPIRE | INNOVATE | DELIVER which can be incorporated into the card
Nice to have
• Use of blues and grey colours
• Compatible with similar styling to our website fennickexecutive.co.uk
Should not have
• Must not be overly brash
• Must not contain cartoon characters

```html
<!DOCTYPE html>
<html lang="en">
<head>
<meta charset="utf-8">
<title>Fennick Executive Search – Business Card</title>
<link href="https://fonts.googleapis.com/css2?family=Roboto:wght@300;400;500;700&display=swap" rel="stylesheet">
<style>
  :root {
    --navy-top: #02071d;
    --navy-bottom: #333649;
    --navy-ink: #1c1f3a;
    --paper: #ffffff;
    --backdrop: #eceae5;
    --grey-text: #55576a;
    --rule: #1c1f3a;
  }
  * { box-sizing: border-box; margin: 0; padding: 0; }
  html, body { width: 1200px; height: 929px; overflow: hidden; }
  body {
    background: var(--backdrop);
    font-family: "Roboto", sans-serif;
    display: flex;
    flex-direction: column;
    align-items: center;
    justify-content: center;
    gap: 56px;
  }
  .card {
    width: 630px;
    height: 360px;
    position: relative;
    box-shadow: 0 6px 18px rgba(0,0,0,0.18);
  }
  .card__frame {
    position: absolute;
    inset: 20px;
    border: 1.5px solid;
  }

  /* Name mark: one weight, one colour, left aligned */
  .wordmark {
    font-weight: 500;
    font-size: 30px;
    line-height: 1.08;
    letter-spacing: 0.01em;
    text-transform: uppercase;
    text-align: left;
  }

  /* Front */
  .card--front {
    background: linear-gradient(180deg, var(--navy-top) 0%, var(--navy-bottom) 100%);
    color: var(--paper);
  }
  .card--front .card__frame { border-color: rgba(255,255,255,0.85); }
  .front__brand {
    position: absolute;
    left: 190px;
    top: 128px;
    text-align: left;
  }
  .front__tagline {
    margin-top: 6px;
    font-size: 12.5px;
    font-weight: 500;
    letter-spacing: 0.02em;
  }

  /* Back */
  .card--back { background: var(--paper); color: var(--navy-ink); }
  .card--back .card__frame { border-color: var(--rule); }
  .back__brand {
    position: absolute;
    left: 62px;
    top: 176px;
    width: 280px;
  }
  .back__brand .wordmark { font-size: 25px; color: var(--navy-ink); }
  .back__slogan {
    margin-top: 5px;
    font-size: 10px;
    font-weight: 700;
    letter-spacing: 0.03em;
  }
  .back__divider {
    position: absolute;
    left: 352px;
    top: 82px;
    width: 1.5px;
    height: 196px;
    background: var(--rule);
  }
  .contact {
    position: absolute;
    left: 372px;
    top: 84px;
    width: 240px;
  }
  .contact__name {
    font-size: 15px;
    font-weight: 700;
    text-transform: uppercase;
    letter-spacing: 0.02em;
  }
  .contact__role { font-size: 12.5px; font-weight: 700; margin-top: 2px; }
  .contact__address {
    margin-top: 16px;
    font-size: 12px;
    font-weight: 300;
    color: var(--grey-text);
    line-height: 1.4;
  }
  .contact__list { list-style: none; margin-top: 10px; }
  .contact__item {
    display: flex;
    align-items: center;
    gap: 9px;
    font-size: 12px;
    font-weight: 300;
    color: var(--grey-text);
    line-height: 1.5;
  }
  .contact__icon { width: 11px; height: 11px; flex: none; fill: var(--navy-ink); }
</style>
</head>
<body>

<section class="card card--front" aria-label="Card front">
  <div class="card__frame"></div>
  <div class="front__brand">
    <div class="wordmark">Fennick<br>Executive Search</div>
    <p class="front__tagline">Exclusively Sourcing &amp; Hiring Senior Leaders</p>
  </div>
</section>

<section class="card card--back" aria-label="Card back">
  <div class="card__frame"></div>
  <div class="back__brand">
    <div class="wordmark">Fennick<br>Executive Search</div>
    <p class="back__slogan">CONSULT | INSPIRE | INNOVATE | DELIVER</p>
  </div>
  <div class="back__divider"></div>
  <div class="contact">
    <p class="contact__name">Gordon Pellbury</p>
    <p class="contact__role">Managing Director</p>
    <p class="contact__address">58 Lindmoor Court, Hatherley Road,<br>Bristol, BS32 9QJ</p>
    <ul class="contact__list">
      <li class="contact__item">
        <svg class="contact__icon" viewBox="0 0 12 12"><path d="M2.5 1 L4.5 1 L5.2 3.6 L4 4.6 Q5 7 7.4 8 L8.4 6.8 L11 7.5 L11 9.5 Q10.5 11 9 11 Q1 10 1 2.5 Q1 1 2.5 1Z"/></svg>
        07823 906417
      </li>
      <li class="contact__item">
        <svg class="contact__icon" viewBox="0 0 12 12"><path d="M3 0.5 H9 V11.5 H3Z M4 1.8 V9 H8 V1.8Z M5.5 9.8 H6.5 V10.8 H5.5Z" fill-rule="evenodd"/></svg>
        0117 486 7132
      </li>
      <li class="contact__item">
        <svg class="contact__icon" viewBox="0 0 12 12"><path d="M0.5 2.5 H11.5 V9.5 H0.5Z"/><path d="M0.8 2.8 L6 6.8 L11.2 2.8" fill="none" stroke="#fff" stroke-width="1"/></svg>
        gordon@fennickexecutive.co.uk
      </li>
      <li class="contact__item">
        <svg class="contact__icon" viewBox="0 0 12 12"><g fill="none" stroke="#1c1f3a" stroke-width="1"><circle cx="6" cy="6" r="5"/><ellipse cx="6" cy="6" rx="2.2" ry="5"/><path d="M1 6 H11 M2 3.5 H10 M2 8.5 H10"/></g></svg>
        fennickexecutive.co.uk
      </li>
    </ul>
  </div>
</section>

</body>
</html>
```